Animal Horse & Bedding Company Needs a Website Coded & Designed

We need a website for a new animal bedding and feed company that is visually grabbing and vibrant. We would like to see a website that displays trust, quality and confidence. Needs to be responsive and mobile friendly for all browsers and coded for both Android & IOS. SEO is also important.

Joomla or Wordpress – must be both desktop and mobile friendly with fast page load speed. Need the ability to edit ourselves in Wordpress or Joomla.

Full details attached below with some layout and content ideas.

Coding

Coded - Design and coding required

Number of Pages Required

5+ page

Font styles to use
Sans Serif

Requirements
Must have
• Needs to be responsive and mobile friendly for all browsers and coded for both Android & IOS. SEO is also important.

Wordpress – must be both desktop and mobile friendly with fast page load speed. Need the ability to edit ourselves in Wordpress.

Logo Colours:
Dark Brown
CMYK: 50 / 70 / 80 / 70
Pantone: 4625C

Orange
CMYK: 0 / 50 / 100 / 0
Pantone: 144C
Nice to have
• Use picture of building attached and super impose logo on building.

```html
<!DOCTYPE html>
<html lang="en">
<head>
<meta charset="utf-8">
<title>Contact Us – Haybarn Supply</title>
<link href="https://fonts.googleapis.com/css2?family=Montserrat:wght@400;500;600;700;800&display=swap" rel="stylesheet">
<style>
:root{
  --orange:#f7931e;
  --brown:#3d2416;
  --ink:#1a1a1a;
  --text:#555;
  --muted:#8a8a8a;
  --line:#cfcfcf;
  --footer:#f4f4f4;
  --white:#fff;
}
*{box-sizing:border-box;margin:0;padding:0}
html,body{width:907px;height:1200px;overflow:hidden;background:var(--white);font-family:'Montserrat',sans-serif;color:var(--ink)}
.page{position:relative;width:907px;height:1200px}
.abs{position:absolute}

/* header */
.site-header{left:0;top:0;width:907px;height:47px;background:var(--white)}
.brand{left:130px;top:11px;display:flex;align-items:center;gap:6px}
.brand-dot{width:20px;height:20px;border-radius:50%;background:var(--orange)}
.brand-name{font-weight:700;font-size:13px;color:var(--brown);letter-spacing:.5px}
.nav{top:17px;font-size:10px;color:#333}
.nav.active{color:var(--orange)}
.nav.active::after{content:"";position:absolute;left:50%;transform:translateX(-50%);bottom:-7px;width:12px;height:1.5px;background:var(--orange)}
.btn{display:flex;align-items:center;justify-content:center;background:var(--orange);color:var(--white);font-weight:700;border-radius:2px}
.header-quote{left:698px;top:13px;width:78px;height:21px;font-size:9.5px}

/* hero */
.hero{left:0;top:47px;width:907px;height:260px;background:linear-gradient(100deg,#0d0805 0%,#2a1608 30%,#9c5a17 55%,#e79a35 68%,#c17423 82%,#3a200c 100%)}
.hero-title{left:130px;top:106px;font-size:38px;font-weight:700;color:var(--white);letter-spacing:-.5px}
.hero-sub{left:130px;top:161px;width:240px;font-size:12px;line-height:12.3px;color:var(--white)}
.hero-quote{left:130px;top:219px;width:79px;height:21px;font-size:10px}

/* contact form */
.section-title{left:0;top:375px;width:907px;text-align:center;font-size:20px;font-weight:700;letter-spacing:-.3px}
.section-lead{left:205px;top:411px;width:497px;text-align:center;font-size:8px;line-height:11.5px;color:var(--muted)}
.field{border:1px solid var(--line);border-radius:3px;background:var(--white);font-size:7.8px;color:#aaa;padding:0 11px;display:flex;align-items:center}
.field.area{align-items:flex-start;padding-top:10px}
.send{left:384px;top:660px;width:149px;height:28px;font-size:10px;font-weight:600;border-radius:3px}

/* map */
.map{left:0;top:762px;width:907px;height:198px;background:linear-gradient(90deg,#a9d3ad 0%,#cfe3cf 30%,#e6e7ea 50%,#e3e4e7 80%,#9fc0f5 100%)}

/* footer */
.site-footer{left:0;top:960px;width:907px;height:240px;background:var(--footer)}
.footer-brand{left:130px;top:1035px;display:flex;align-items:center;gap:6px}
.footer-about{left:130px;top:1086px;width:125px;font-size:7px;line-height:8.5px;color:var(--text)}
.footer-head{top:1024px;font-size:12px;font-weight:600}
.footer-link{font-size:7px;color:var(--text)}
.social{top:1048px;width:9px;height:9px;border-radius:50%;background:#666}
.social.on{background:var(--orange)}
.subscribe-field{left:627px;top:1076px;width:149px;height:22px;background:var(--white);display:flex;align-items:center;gap:6px;padding-left:8px;font-size:6.5px;color:#aaa}
.mail-icon{width:7px;height:6px;background:var(--orange);border-radius:1px}
.subscribe-btn{left:627px;top:1101px;width:149px;height:21px;font-size:6.5px;font-weight:500;border-radius:2px}
.footer-rule{left:0;top:1163px;width:907px;height:1px;background:#cfcfcf}
.copyright{left:0;top:1178px;width:907px;text-align:center;font-size:7px;color:#333}
</style>
</head>
<body>
<div class="page">
  <header class="site-header abs"></header>
  <div class="brand abs"><span class="brand-dot"></span><span class="brand-name">HAYBARN SUPPLY</span></div>
  <span class="nav abs" style="left:413px">Home</span>
  <span class="nav abs" style="left:465px">About Us</span>
  <span class="nav abs" style="left:531px">Feed</span>
  <span class="nav abs" style="left:578px">Bedding</span>
  <span class="nav active abs" style="left:641px">Contact</span>
  <a class="btn header-quote abs">Get a Quote</a>

  <section class="hero abs" role="img" aria-label="Photo of two farmers shaking hands in a field at sunset"></section>
  <h1 class="hero-title abs">Contact Us</h1>
  <p class="hero-sub abs">Haybarn Supply offers supply and delivery of fresh bedding as well as removal of waste bedding.</p>
  <a class="btn hero-quote abs">Get a Quote</a>

  <h2 class="section-title abs">Get In Touch</h2>
  <p class="section-lead abs">Lorem Ipsum is simply dummy text of the printing and typesetting industry. Lorem Ipsum has been the industry's standard dummy text ever since the 1500s, when an unknown printer took a galley of type and scrambled it to make a type specimen book.</p>

  <div class="field abs" style="left:159px;top:464px;width:288px;height:28px">First Name*</div>
  <div class="field abs" style="left:460px;top:464px;width:288px;height:28px">Last Name*</div>
  <div class="field abs" style="left:159px;top:501px;width:288px;height:28px">Email Address*</div>
  <div class="field abs" style="left:460px;top:501px;width:288px;height:28px">Contact Number*</div>
  <div class="field area abs" style="left:160px;top:539px;width:588px;height:105px">Requirements*</div>
  <a class="btn send abs">Send Message</a>

  <div class="map abs" role="img" aria-label="Street map showing the company location and surrounding suburbs"></div>

  <footer class="site-footer abs"></footer>
  <div class="footer-brand abs"><span class="brand-dot"></span><span class="brand-name">HAYBARN SUPPLY</span></div>
  <p class="footer-about abs">Ready to start a new project or curious about our process? Drop us a note or give us a call. We are happy to answer any questions and provide a free consultation.</p>

  <h3 class="footer-head abs" style="left:328px">Menu</h3>
  <span class="footer-link abs" style="left:329px;top:1053px">Home</span>
  <span class="footer-link abs" style="left:329px;top:1069px">About us</span>
  <span class="footer-link abs" style="left:329px;top:1085px">Feed</span>
  <span class="footer-link abs" style="left:329px;top:1102px">Badding</span>
  <span class="footer-link abs" style="left:329px;top:1118px">Contact</span>

  <h3 class="footer-head abs" style="left:457px">Contact Us</h3>
  <span class="footer-link abs" style="left:457px;top:1053px;line-height:10.5px;width:100px">Haybarn Supply<br>218 Meadow Lane #12, Fairview, OR 97024</span>
  <span class="footer-link abs" style="left:457px;top:1090px">555-014-2290</span>
  <span class="footer-link abs" style="left:457px;top:1106px">hello@haybarnsupply.com</span>

  <h3 class="footer-head abs" style="left:627px">Social Media</h3>
  <span class="social abs" style="left:627px"></span>
  <span class="social on abs" style="left:642px"></span>
  <span class="social abs" style="left:660px"></span>
  <span class="social abs" style="left:678px"></span>
  <span class="social abs" style="left:696px"></span>
  <div class="subscribe-field abs"><span class="mail-icon"></span>Email Address</div>
  <a class="btn subscribe-btn abs">Subscribe Now</a>

  <div class="footer-rule abs"></div>
  <p class="copyright abs">©2021 haybarnsupply. All Rights Reserved.</p>
</div>
</body>
</html>
```